Business Cards for our company

Hi there,

we have successfully designed a logo with ArtFlock and would like now to design our business cards. We would like to keep the colours and the look-and-feel of the logo. Please send in variations with two or three colours and one or two sides. I promise to respond to every single submission.

Many thanks and happy new year.

All the best,
Wilfried

Target Market(s)

B2B

Industry/Entity Type

Trade

Contact Information for Business Card

We have successfully designed a logo with ArtFlock and would like now to design our business cards. We would like to keep the colours and the look-and-feel of the logo. Please send in variations with two or three colours and one or two sides. I promise to respond to every single submission.

Font styles to use
Serif
Sans Serif
Script

Requirements
Must have
• These information should be on the business card, grouped as you suggest, and we think using small pictograms for mobile, email, etc is pretty helpful:
• Wilfried Tammler (first and second name)
• Geschäftsführer/ Managing Director (title)
• KoR Warenkontor GmbH (company name and legal form)
• Ostheimer Str. 18/3 (street and house number)
• 31547 Lindenau (zip code and town)
• +491709384562 (mobile)
• +4955519027341 (work)
• w.tammler@kor-warenkontor.example (email)
• www.kor-warenkontor.example (web)
Nice to have
• Spectacular and interesting layout and design. You look at it and think, wow, that's not the normal stuff.
• We think of ourselves as bridge-builders between businesses (international producers on the one hand, and retail chains on the other hand) and we translate, organise and manage projects where both partners are involved, but it's difficult for them to cooperate due to language barriers and different working cultures.
• This is why we have the n between the B's shaped as a bridge, and the green arc supports this idea. Maybe you could play with this idea...
Should not have
• the standard layout that everybody has

```html
<!DOCTYPE html>
<html lang="de">
<head>
<meta charset="utf-8">
<title>KoR Warenkontor – Visitenkarte</title>
<link href="https://fonts.googleapis.com/css2?family=Noto+Sans:wght@300;400;600;700&display=swap" rel="stylesheet">
<style>
  :root {
    --backdrop: #d1d3d4;
    --card-white: #ffffff;
    --brand-green: #2ead4b;
    --arc-grey: #e5e6e7;
    --ink: #111111;
    --on-green: #ffffff;
  }
  * { margin: 0; padding: 0; box-sizing: border-box; }
  html, body {
    width: 1200px; height: 1155px; overflow: hidden;
    background: var(--backdrop);
    font-family: "Noto Sans", Arial, sans-serif;
  }
  .card {
    position: absolute; left: 375px; top: 218px;
    width: 450px; height: 745px;
    border-radius: 225px; overflow: hidden;
    background: var(--card-white);
  }
  .card-shapes { position: absolute; inset: 0; }
  .wordmark {
    position: absolute; left: 0; right: 0; top: 66px;
    text-align: center; color: var(--ink); font-weight: 700;
  }
  .wordmark-short { display: block; font-size: 100px; line-height: 1; letter-spacing: 2px; }
  .wordmark-long { display: block; font-size: 28px; line-height: 1.2; letter-spacing: 3px; margin-top: 4px; }
  .contact {
    position: absolute; left: 0; right: 0; top: 377px;
    text-align: center; color: var(--on-green);
  }
  .person-name { font-size: 22px; font-weight: 700; line-height: 1.1; }
  .person-title { font-size: 17px; font-weight: 300; margin-top: 5px; line-height: 1.2; }
  .contact-icon { display: block; margin: 13px auto 5px; width: 14px; height: 14px; fill: var(--on-green); }
  .contact-line { font-size: 18px; font-weight: 600; line-height: 25px; }
  .contact-line.web { font-size: 17px; }
  .contact-icon.tight { margin: 2px auto 3px; }
</style>
</head>
<body>
  <div class="card">
    <svg class="card-shapes" width="450" height="745" viewBox="0 0 450 745" aria-hidden="true">
      <circle cx="225" cy="483" r="228" fill="var(--arc-grey)"/>
      <circle cx="225" cy="480" r="177" fill="var(--brand-green)"/>
      <rect x="0" y="350" width="450" height="395" fill="var(--brand-green)"/>
    </svg>

    <div class="wordmark">
      <span class="wordmark-short">KoR</span>
      <span class="wordmark-long">WARENKONTOR</span>
    </div>

    <div class="contact">
      <p class="person-name">WILFRIED TAMMLER</p>
      <p class="person-title">Geschäftsführer</p>

      <svg class="contact-icon" viewBox="0 0 14 14" aria-hidden="true"><path d="M7 0a5 5 0 0 0-5 5c0 3.5 5 9 5 9s5-5.5 5-9a5 5 0 0 0-5-5zm0 7a2 2 0 1 1 0-4 2 2 0 0 1 0 4z"/></svg>
      <p class="contact-line">Ostheimer Str. 18/3</p>
      <p class="contact-line">31547 Lindenau</p>

      <svg class="contact-icon" viewBox="0 0 14 14" aria-hidden="true"><circle cx="7" cy="7" r="7"/><path d="M4.5 3.5l1.6-.4.8 2-1 .8a5 5 0 0 0 2.2 2.2l.8-1 2 .8-.4 1.6C8 10 4 6 4.5 3.5z" fill="var(--brand-green)"/></svg>
      <p class="contact-line">+491709384562</p>
      <p class="contact-line">+4955519027341</p>

      <svg class="contact-icon tight" viewBox="0 0 14 14" aria-hidden="true"><circle cx="7" cy="7" r="7"/><path d="M3.5 4.5h7v5h-7z" fill="var(--brand-green)"/><path d="M3.5 4.5L7 7.5l3.5-3" stroke="var(--on-green)" fill="none" stroke-width="1"/></svg>
      <p class="contact-line web">w.tammler@kor-warenkontor.example</p>

      <svg class="contact-icon tight" viewBox="0 0 14 14" aria-hidden="true"><g fill="none" stroke="var(--on-green)" stroke-width="1.2"><circle cx="7" cy="7" r="6"/><ellipse cx="7" cy="7" rx="2.6" ry="6"/><path d="M1 7h12M2 4h10M2 10h10"/></g></svg>
      <p class="contact-line web">www.kor-warenkontor.example</p>
    </div>
  </div>
</body>
</html>
```